Veterinary Business cards

Redesign Business Card

Information needed on Card:
Hours: Mon-Fri: 4pm -10PM; Sat- Sun- 10 AM- 5PM
Help@bayfernvet.com
www.bayfernvet.com
555-718-2946
4173 SE 19th Ave. okc, ok 73958
*No appointment necessary*

Optional:
Our tag line is "We're here when you need us" - If it fits on the cards.

```html
<!DOCTYPE html>
<html lang="en">
<head>
<meta charset="utf-8">
<title>Bayfern Urgent Care – Business Cards</title>
<link rel="stylesheet" href="https://fonts.googleapis.com/css2?family=Noto+Serif:wght@400;500&display=swap">
<style>
  :root {
    --stage: #111111;
    --paper: #f7f7f7;
    --mint-dark: #6fd4a8;
    --mint-light: #88e9c7;
    --navy: #1f5799;
    --gold: #efb22e;
    --white: #ffffff;
  }
  * { margin: 0; padding: 0; box-sizing: border-box; }
  html, body { width: 1200px; height: 800px; overflow: hidden; }
  body {
    background: var(--stage);
    font-family: "Noto Serif", Georgia, serif;
    display: flex;
    align-items: center;
    justify-content: center;
    gap: 40px;
  }
  .card {
    position: relative;
    width: 540px;
    height: 308px;
    border-radius: 24px;
    overflow: hidden;
    background: var(--paper);
  }
  .card-art { position: absolute; inset: 0; width: 100%; height: 100%; }

  .brand { position: absolute; text-align: left; }
  .brand-name {
    color: var(--navy);
    font-weight: 400;
    font-size: 34px;
    letter-spacing: 2px;
    line-height: 1;
    display: flex;
    align-items: center;
    gap: 10px;
  }
  .brand-dot {
    width: 12px; height: 12px; border-radius: 50%;
    background: var(--gold);
    display: inline-block;
  }
  .brand-sub {
    color: var(--navy);
    font-size: 11px;
    letter-spacing: 3px;
    margin-top: 4px;
    border-bottom: 1px solid var(--navy);
    padding-bottom: 3px;
    display: inline-block;
  }
  .tagline { color: var(--gold); font-size: 15px; margin-top: 6px; }

  /* front */
  .front .brand { top: 26px; right: 44px; }
  .front .note {
    position: absolute; right: 40px; bottom: 70px;
    color: var(--navy); font-size: 16px;
  }

  /* back */
  .back .brand { top: 92px; right: 30px; }
  .back .brand-name { font-size: 28px; }
  .back .tagline { font-size: 13px; }
  .hours {
    position: absolute; left: 34px; top: 96px;
    color: var(--white); font-size: 15px; line-height: 1.6;
  }
  .contact {
    position: absolute; left: 34px; bottom: 30px;
    list-style: none; color: var(--white); font-size: 11px;
  }
  .contact li { display: flex; align-items: center; gap: 8px; margin-top: 6px; }
  .contact svg { width: 12px; height: 12px; fill: var(--white); flex: none; }
</style>
</head>
<body>

  <section class="card front" aria-label="Card front">
    <svg class="card-art" viewBox="0 0 540 308" preserveAspectRatio="none" aria-hidden="true">
      <defs>
        <linearGradient id="mintFront" x1="0" y1="1" x2="1" y2="0">
          <stop offset="0" stop-color="var(--mint-dark)"/>
          <stop offset="1" stop-color="var(--mint-light)"/>
        </linearGradient>
      </defs>
      <path d="M0 262 C 120 160, 260 172, 360 162 C 450 152, 510 126, 540 102 L540 308 L0 308 Z" fill="url(#mintFront)"/>
      <path d="M0 262 C 120 160, 260 172, 360 162 C 450 152, 510 126, 540 102" fill="none" stroke="var(--gold)" stroke-width="2"/>
    </svg>
    <div class="brand">
      <div class="brand-name"><span class="brand-dot"></span>BAYFERN</div>
      <div class="brand-sub">URGENT CARE</div>
      <div class="tagline">We're here when you need us</div>
    </div>
    <p class="note">No appointment necessary</p>
  </section>

  <section class="card back" aria-label="Card back">
    <svg class="card-art" viewBox="0 0 540 308" preserveAspectRatio="none" aria-hidden="true">
      <defs>
        <linearGradient id="mintBack" x1="0" y1="1" x2="1" y2="0">
          <stop offset="0" stop-color="var(--mint-dark)"/>
          <stop offset="1" stop-color="var(--mint-light)"/>
        </linearGradient>
      </defs>
      <rect width="540" height="308" fill="url(#mintBack)"/>
      <circle cx="520" cy="40" r="275" fill="var(--paper)"/>
    </svg>
    <div class="brand">
      <div class="brand-name"><span class="brand-dot"></span>BAYFERN</div>
      <div class="brand-sub">URGENT CARE</div>
      <div class="tagline">We're here when you need us</div>
    </div>
    <p class="hours">Hours: Mon-Fri: 4pm-10pm;<br>Sat-Sun: 10am-5pm</p>
    <ul class="contact">
      <li><svg viewBox="0 0 12 12"><path d="M0 2h12v8H0z M1 3l5 4 5-4" fill="none" stroke="#fff" stroke-width="1.2"/></svg>Help@bayfernvet.com</li>
      <li><svg viewBox="0 0 12 12"><circle cx="6" cy="6" r="5" fill="none" stroke="#fff"/><path d="M1 6h10M6 1c-3 3-3 7 0 10M6 1c3 3 3 7 0 10" fill="none" stroke="#fff"/></svg>www.bayfernvet.com</li>
      <li><svg viewBox="0 0 12 12"><path d="M2 1l2.5 0 1 3-1.5 1a6 6 0 0 0 3 3l1-1.5 3 1V10a1 1 0 0 1-1 1A10 10 0 0 1 1 2a1 1 0 0 1 1-1z"/></svg>555-718-2946</li>
      <li><svg viewBox="0 0 12 12"><path d="M6 0a4 4 0 0 1 4 4c0 3-4 8-4 8S2 7 2 4a4 4 0 0 1 4-4z"/><circle cx="6" cy="4" r="1.4" fill="var(--mint-dark)"/></svg>4173 SE 19th Ave. okc,ok 73958</li>
    </ul>
  </section>

</body>
</html>
```